Podiatry clinic requires a modern revamp and editing of existing website.

I would like a fresh new look and updated information for my current business website. An easy to navigate site with prominent address and phone number for call to action. We are a podiatry clinic that focuses on general and sports podiatry.
I would like 4 pages; including Home page, About Us, Services & Contact.
www.brambleridgefootcare.com

Target Market(s)

Active working professionals.

Industry/Entity Type

Medical

Coding

Coded - Design and coding required

Number of Pages Required

4 page

Font styles to use
Sans Serif

Colors
6b449b

Requirements
Must have
• A modern look with logo and active images; clean and uncluttered. Visible phone number and address for call to action.
• 4 pages - Home, About Us, Services, Contact.
• Home page - update address & service logos.
• About Us - update of personal information.
• Services - Revamp of existing page.
• Contact page to include Searchly map, email & phone number.
Nice to have
• Ability to add content easily; eg. a blog or adding video onto Home page.
• Link to Friendsheet page.

```html
<!DOCTYPE html>
<html lang="en">
<head>
<meta charset="utf-8">
<title>Brambleridge Foot Care</title>
<link href="https://fonts.googleapis.com/css2?family=Cabin:wght@500;600&family=Lato:ital,wght@0,400;0,700;1,400&display=swap" rel="stylesheet">
<style>
:root{
  --purple:#9b87c4;
  --purple-dark:#6b449b;
  --orange:#f47a2c;
  --orange-panel:#ee8a4e;
  --green:#8cc63f;
  --green-panel:#93c85a;
  --ink:#111;
  --grey-bg:#eeeeee;
  --footer:#050505;
  --white:#fff;
}
*{box-sizing:border-box;margin:0;padding:0}
html,body{width:693px;height:1200px;overflow:hidden;background:var(--white)}
body{font-family:"Lato",sans-serif;color:var(--ink);position:relative}
.abs{position:absolute}
h1,h2,h3,h4{font-family:"Cabin",sans-serif;font-weight:600}

/* header */
.site-header{position:absolute;left:0;top:0;width:693px;height:77px;background:var(--purple)}
.brand{left:40px;top:22px;display:flex;align-items:center;gap:7px;color:var(--white);font-family:"Cabin",sans-serif;font-weight:600;font-size:15px}
.brand-mark{width:22px;height:22px;border-radius:50%;background:var(--purple-dark)}
.top-contact{top:11px;display:flex;align-items:center;gap:6px;color:var(--white);font-size:9.5px}
.icon-dot{width:18px;height:18px;border-radius:50%;background:var(--green);display:flex;align-items:center;justify-content:center}
.main-nav{top:54px;left:302px;display:flex;gap:0;font-size:10px;color:var(--white)}
.main-nav a{color:inherit;text-decoration:none;margin-right:27px}
.btn-book{left:544px;top:48px;width:113px;height:21px;background:var(--orange);color:var(--white);font-size:9.5px;display:flex;align-items:center;justify-content:center;border-radius:2px}

/* hero */
.hero-photo{left:0;top:77px;width:693px;height:303px;background:linear-gradient(110deg,#3a3f4a 0%,#c9b6a6 30%,#e8d3c2 55%,#9a8e86 80%,#d8dbe0 100%)}
.hero-arrow{top:182px;width:22px;height:31px;background:#555;display:flex;align-items:center;justify-content:center}
.hero-caption{left:0;top:340px;width:693px;height:40px;background:rgba(0,0,0,.88);color:var(--white);font-family:"Cabin",sans-serif;font-weight:500;font-size:18.5px;display:flex;align-items:center;justify-content:center}

/* welcome */
.welcome-title{left:0;top:398px;width:693px;text-align:center;font-size:18.5px;font-weight:500}
.t-orange{color:var(--orange)}.t-green{color:var(--green)}
.welcome-rule{left:163px;top:430px;width:366px;height:1px;background:#999}
.welcome-text{left:38px;top:442px;width:617px;text-align:center;font-size:9.1px;line-height:15.5px;color:#222}
.btn{height:21px;color:var(--white);font-size:8px;font-weight:700;display:flex;align-items:center;justify-content:center;gap:4px;border-radius:2px}
.btn-orange{background:var(--orange)}
.btn-green{background:var(--green)}
.btn-black{background:#000}

/* service panels */
.panel{top:545px;height:247px}
.panel-general{left:0;width:343px;background:linear-gradient(135deg,#f09a66,#ec7c3c 60%,#e7894c)}
.panel-sports{left:343px;width:350px;background:linear-gradient(135deg,#9dcd6b,#8ec452 60%,#a3d270)}
.panel-badge{width:74px;height:74px;border-radius:50%;top:33px;border:2px solid var(--white)}
.panel h3{position:absolute;top:117px;width:100%;text-align:center;color:var(--white);font-size:18px;font-weight:500}
.panel p{position:absolute;top:144px;left:55px;right:55px;text-align:center;color:var(--white);font-size:7.7px;font-weight:700;line-height:14px}

/* lower band */
.lower{left:0;top:792px;width:693px;height:223px;background:var(--grey-bg)}
.testimonial-side{left:0;top:792px;width:343px;height:223px;background:linear-gradient(90deg,#f1f1f1,#e2e2e2)}
.section-title{font-size:17.5px;font-weight:500}
.quote{left:110px;top:857px;width:200px;font-size:8.6px;font-style:italic;line-height:14.6px;color:#222;letter-spacing:.2px}
.client-photo{left:37px;top:865px;width:66px;height:66px;border-radius:50%;border:3px solid var(--white);background:linear-gradient(160deg,#8a6b55,#d4b196 55%,#2d3b6b);box-shadow:0 1px 4px rgba(0,0,0,.25)}
.partner{background:var(--white);border:1px solid #cfcfcf;display:flex;align-items:center;justify-content:center}

/* footer */
.site-footer{left:0;top:1015px;width:693px;height:158px;background:var(--footer);color:var(--white)}
.foot-title{position:absolute;top:19px;font-size:11px;font-weight:500;color:var(--white)}
.foot-rule{position:absolute;top:33px;height:1px;background:#333}
.foot-text{position:absolute;font-size:7.4px;line-height:9px;color:#e8e8e8}
.foot-list{position:absolute;list-style:none;font-size:7.4px;color:#e8e8e8}
.foot-list li{height:17.6px;display:flex;align-items:center;gap:7px}
.foot-list li::before{content:"";width:3px;height:3px;border-radius:50%;background:var(--green)}
.social{position:absolute;left:589px;display:flex;align-items:center;gap:7px;font-size:7.6px;font-weight:700}
.social i{width:19px;height:19px;border-radius:50%;display:block}
.copyright{left:0;top:1173px;width:693px;height:27px;background:var(--orange);color:var(--white);font-size:7.5px;display:flex;align-items:center;justify-content:center}
</style>
</head>
<body>

<header class="site-header">
  <div class="abs brand"><span class="brand-mark"></span>Brambleridge Foot Care</div>
  <div class="abs top-contact" style="left:404px">
    <span class="icon-dot"><svg width="9" height="7" viewBox="0 0 9 7"><rect x=".5" y=".5" width="8" height="6" fill="none" stroke="#fff"/><path d="M.5 .5 4.5 4 8.5 .5" fill="none" stroke="#fff"/></svg></span>
    info@brambleridgefootcare.com
  </div>
  <div class="abs top-contact" style="left:572px">
    <span class="icon-dot"><svg width="9" height="9" viewBox="0 0 10 10"><path d="M2 1l2 2-1 1.2c.6 1.3 1.5 2.2 2.8 2.8L7 6l2 2-1.3 1.3C4.5 9 1 5.5.7 2.3z" fill="#fff"/></svg></span>
    1300 555 274
  </div>
  <nav class="abs main-nav"><a>Home</a><a>About Us</a><a>Services</a><a>Contact</a></nav>
  <div class="abs btn-book">Book An Appointment</div>
</header>

<section>
  <div class="abs hero-photo" role="img" aria-label="Podiatrist examining a patient's foot and fitting an orthotic insole"></div>
  <div class="abs hero-arrow" style="left:0"><svg width="8" height="12" viewBox="0 0 8 12"><path d="M6.5 1 1.5 6l5 5" fill="none" stroke="#fff" stroke-width="2"/></svg></div>
  <div class="abs hero-arrow" style="left:671px"><svg width="8" height="12" viewBox="0 0 8 12"><path d="M1.5 1l5 5-5 5" fill="none" stroke="#fff" stroke-width="2"/></svg></div>
  <h1 class="abs hero-caption">Brambleridge Foot Care Is A Podiatry Clinic In The Heart Of Melbourne</h1>
</section>

<section>
  <h2 class="abs welcome-title">Welcome To <span class="t-orange">Brambleridge</span> Foot <span class="t-green">Care</span></h2>
  <div class="abs welcome-rule"></div>
  <p class="abs welcome-text">Ut wisi enim adi minim veniam, quis nostrudk exerci tation more ullamcorper suscipit lobortis nis ut aliquip commodo conseqti. Duis autem iriure dolor in hendrerit in vulputate veesseml molestie consequat, vel illum facilisi. Lorem ipsum dolor sit amet, conse ctetuer adipiscing elit, sedmoi di nonummy nibh &nbsp;commodo consequat. Duis autem vel eum iriurel dolor in hendrerit.</p>
  <div class="abs btn btn-orange" style="left:312px;top:500px;width:69px">Read More <span>»</span></div>
</section>

<section>
  <div class="abs panel panel-general" role="img" aria-label="Warm-toned photo of a foot treatment">
    <div class="abs panel-badge" style="left:139px;background:var(--green)"></div>
    <h3>General Podiatry</h3>
    <p>Lorem ipsum dolor sit amet, consectetuer adipiscing elit, seddiam nonummy nibh euismod tincidunt ut laoreetfgf doloremagna aliquam erat volutpat.</p>
    <div class="abs btn btn-green" style="left:142px;top:198px;width:70px">Read More <span>»</span></div>
  </div>
  <div class="abs panel panel-sports" role="img" aria-label="Green-toned photo of an athlete training">
    <div class="abs panel-badge" style="left:144px;background:#000"></div>
    <h3>Sports Podiatry</h3>
    <p>Lorem ipsum dolor sit amet, consectetuer adipiscing elit, seddiam nonummy nibh euismod tincidunt ut laoreetfgf doloremagna aliquam erat volutpat.</p>
    <div class="abs btn btn-black" style="left:146px;top:198px;width:70px">Read More <span>»</span></div>
  </div>
</section>

<section>
  <div class="abs lower"></div>
  <div class="abs testimonial-side"></div>
  <svg class="abs" style="left:35px;top:814px" width="20" height="18" viewBox="0 0 20 18"><ellipse cx="8" cy="6.5" rx="8" ry="6" fill="#333"/><path d="M3 11 2 16l5-4z" fill="#333"/><ellipse cx="13" cy="10" rx="6" ry="4.5" fill="#555"/></svg>
  <h2 class="abs section-title" style="left:63px;top:812px">Client <span class="t-orange">Testimonials</span></h2>
  <svg class="abs" style="left:298px;top:819px" width="28" height="10" viewBox="0 0 28 10"><path d="M5 1 1.5 5 5 9" fill="none" stroke="#111" stroke-width="1.8"/><path d="M18 1l3.5 4L18 9" fill="none" stroke="var(--orange)" stroke-width="1.8"/></svg>
  <div class="abs client-photo" role="img" aria-label="Portrait of client"></div>
  <div class="abs" style="left:106px;top:851px;font-family:Georgia,serif;font-size:26px;color:#999;line-height:1">“</div>
  <p class="abs quote">&nbsp;&nbsp;&nbsp;&nbsp;&nbsp;&nbsp;Lorem ipsum dolor sit amet, consectetuer adipiscing elit, sed diam nonummy nibh euismod tincidunt ut laoreet dolore magna aliquam erat volutpat. Ut wisi enim ad minim veniam, quis nostrud exerci tation ullamcorper suscipit lobortis nisl ut aliquip</p>
  <div class="abs" style="left:110px;top:952px;width:90px;height:1px;background:#bbb"></div>
  <div class="abs t-orange" style="left:110px;top:959px;font-family:Cabin,sans-serif;font-size:12px;font-weight:500">Loren Ipsum</div>
  <div class="abs" style="left:110px;top:975px;font-size:8px">Marketing Manager</div>

  <svg class="abs" style="left:364px;top:813px" width="22" height="20" viewBox="0 0 22 20"><circle cx="11" cy="10" r="9" fill="none" stroke="#444" stroke-width="1"/><path d="M5 10h12" stroke="#444"/></svg>
  <h2 class="abs section-title" style="left:398px;top:812px">Our <span class="t-orange">Affiliations</span></h2>
  <div class="abs" style="left:360px;top:838px;width:300px;height:1px;background:#ddd"></div>
  <div class="abs partner" style="left:406px;top:853px;width:207px;height:65px"><div style="width:150px;height:26px;background:#f6c400;border-radius:3px"></div></div>
  <div class="abs partner" style="left:378px;top:931px;width:111px;height:54px"><div style="width:80px;height:28px;background:#1b5aa6;border-radius:3px"></div></div>
  <div class="abs partner" style="left:529px;top:931px;width:112px;height:54px"><div style="width:30px;height:30px;background:#f3b21b;border-radius:50%"></div></div>
</section>

<footer class="abs site-footer">
  <h4 class="foot-title" style="left:36px">Quick <span class="t-green">Links</span></h4>
  <div class="foot-rule" style="left:36px;width:79px"></div>
  <ul class="foot-list" style="left:36px;top:40px"><li>Home</li><li>About Us</li><li>Services</li><li>Contact &nbsp;Us</li></ul>

  <h4 class="foot-title" style="left:190px">Contact <span class="t-green">Details</span></h4>
  <div class="foot-rule" style="left:190px;width:137px"></div>
  <svg class="abs" style="left:189px;top:46px" width="7" height="9" viewBox="0 0 7 9"><path d="M3.5 9S0 5 0 3.5a3.5 3.5 0 0 1 7 0C7 5 3.5 9 3.5 9z" fill="var(--green)"/><circle cx="3.5" cy="3.5" r="1.3" fill="#000"/></svg>
  <div class="foot-text" style="left:202px;top:45px;font-weight:700">Brambleridge Foot Care</div>
  <div class="foot-text" style="left:202px;top:59px;line-height:11px">Suite 212/95 Larkspur Street<br>Melbourne 3000</div>
  <svg class="abs" style="left:189px;top:94px" width="8" height="8" viewBox="0 0 10 10"><path d="M2 1l2 2-1 1.2c.6 1.3 1.5 2.2 2.8 2.8L7 6l2 2-1.3 1.3C4.5 9 1 5.5.7 2.3z" fill="var(--green)"/></svg>
  <div class="foot-text" style="left:202px;top:93px;font-weight:700">1300 555 274</div>
  <svg class="abs" style="left:189px;top:115px" width="8" height="6" viewBox="0 0 9 7"><rect width="9" height="7" fill="var(--green)"/><path d="M0 0l4.5 4L9 0" fill="none" stroke="#000"/></svg>
  <div class="foot-text" style="left:202px;top:114px;font-weight:700">info@brambleridgefootcare.com</div>

  <div class="foot-rule" style="left:370px;width:22px"></div>
  <h4 class="foot-title" style="left:403px">Hours of <span class="t-green">Operation</span></h4>
  <div class="foot-rule" style="left:403px;width:111px"></div>
  <div class="foot-text" style="left:407px;top:47px;line-height:12px"><b>Monday to Thursday</b><br>10:00 am to 07:00 pm</div>
  <div class="foot-text" style="left:407px;top:79px;line-height:12px"><b>Friday &amp; Satuday</b><br>10:00 am to 05:00 pm</div>
  <div class="foot-text" style="left:407px;top:110px;line-height:12px"><b>Sunday</b><br>10:00 am to 01:00 pm</div>

  <h4 class="foot-title" style="left:589px">Follow <span class="t-green">Us</span></h4>
  <div class="foot-rule" style="left:589px;width:69px"></div>
  <div class="social" style="top:47px"><i style="background:#1f5fa8"></i>FRIENDSHEET</div>
  <div class="social" style="top:73px"><i style="background:#1fa9dd"></i>CHIRPER</div>
  <div class="social" style="top:99px"><i style="background:#1f78b4"></i>WORKLINK</div>
  <div class="social" style="top:125px"><i style="background:#d8432e"></i>SEARCHLY</div>
</footer>

<div class="abs copyright">Copyright © 2016 &nbsp;Brambleridge Foot Care. All Rights Reserved.</div>

</body>
</html>
```